Trade Show booth design

I need the following designs for my trade booth:
1. backboard design 3m Wx2mH
2. Tressle table, tablecloth front panel design 1800W x 740mmH
3. Pop-up banner. I have included our logos and some design content ideas:
Headline:
"Cleaner Classrooms. Safer Schools."
Subheadline:
"Specialist Cleaning Solutions for Education Facilities"
Key Points to Grab Attention:
Healthy Environments: Create hygienic, safe learning spaces for students and staff with our expert cleaning services.
Tailored to Your Needs: Custom cleaning plans for classrooms, labs, libraries, and sports facilities.
Affordable Excellence: Premium results without premium costs – tailored plans mean you only pay for what you need.
Safety First: All staff are trained, highly vetted, and hold current Working with Children Checks (WWCC).
Eco-Conscious Cleaning: Using non-toxic, eco-friendly products certified for health and safety.
What Schools Really Need:
Reliability: Consistent, high-quality cleaning from a trusted provider.
Cost-Effectiveness: Solutions that fit tight budgets while maintaining high standards.
Expertise: Over 30 years of experience in education facility cleaning.
Disinfection Services: Focus on high-touch areas to reduce the spread of germs and ensure peace of mind.
Visual Elements:
Images of bright, clean classrooms, a happy teacher welcoming students, or students collaborating in a spotless library.
Icons representing safety (shield), hygiene (sparkling star), and eco-friendliness (leaf).
Your logo with the tagline: "Trusted by Queensland Schools Since 1995."
Call-to-Action:
"Visit us to discuss your school’s cleaning needs and book a FREE consultation."
Include contact details: Phone: 1300 649 315 | Website: www.duravoss.com.au
Target Market(s)
Education sector
Industry/Entity Type
Commercial Cleaning
Font styles to use
Other font styles liked:
- Montserrat
Look and feel

```html
<!DOCTYPE html>
<html lang="en">
<head>
<meta charset="utf-8">
<title>Duravoss – Education Cleaning Backboard</title>
<link href="https://fonts.googleapis.com/css2?family=Montserrat:wght@400;500;700;800;900&display=swap" rel="stylesheet">
<style>
  :root {
    --navy: #1e3f66;
    --sky: #2f8ad8;
    --ink: #1b1b1b;
    --white: #ffffff;
    --stage: #e8eaed;
  }
  * { box-sizing: border-box; margin: 0; padding: 0; }
  html, body { width: 1200px; height: 1200px; overflow: hidden; }
  body {
    background: var(--stage);
    font-family: "Montserrat", sans-serif;
    color: var(--ink);
    position: relative;
  }
  .backboard {
    position: absolute;
    left: 20px; top: 211px;
    width: 1160px; height: 777px;
    background: var(--white);
    overflow: hidden;
  }
  .brand {
    position: absolute; left: 58px; top: 30px; width: 420px;
  }
  .brand-name {
    display: flex; align-items: center; gap: 16px;
    font-weight: 800; font-size: 62px; color: var(--navy);
    letter-spacing: -1px; line-height: 1;
    height: 110px;
  }
  .brand-dot {
    width: 40px; height: 40px; border-radius: 50%; background: var(--navy);
    flex: none;
  }
  .brand-tagline {
    position: absolute; top: 124px; left: 0;
    font-size: 16px; font-weight: 500; white-space: nowrap; color: var(--ink);
  }
  .headline {
    position: absolute; left: 587px; top: 20px;
    color: var(--navy); font-weight: 800; font-size: 35px; line-height: 43px;
    letter-spacing: -0.3px; white-space: nowrap;
  }
  .subheadline {
    position: absolute; left: 587px; top: 108px;
    font-size: 26px; font-weight: 500; line-height: 35px; color: var(--ink);
    white-space: nowrap;
  }
  .band {
    position: absolute; left: 0; top: 202px; width: 100%; height: 111px;
    background: var(--navy);
  }
  .band-rule {
    position: absolute; left: 0; top: 313px; width: 100%; height: 7px;
    background: var(--sky);
  }
  .feature {
    position: absolute; top: 217px; width: 300px; margin-left: -150px;
    text-align: center;
  }
  .feature-badge {
    width: 140px; height: 140px; margin: 0 auto;
    border-radius: 50%; background: var(--white);
    border: 3px solid var(--navy);
    display: flex; align-items: center; justify-content: center;
  }
  .feature-badge svg { width: 86px; height: 86px; }
  .feature-text {
    margin-top: 16px; font-size: 17.5px; font-weight: 500; line-height: 23px;
    white-space: nowrap;
  }
  .feature-text strong { color: var(--navy); font-weight: 800; }
  .photo {
    position: absolute; top: 428px; height: 216px;
  }
  .photo-classroom { left: 27px; width: 358px; background: linear-gradient(135deg, #d9a34f, #c47f3e 55%, #8fa0b5); }
  .photo-welcome { left: 394px; width: 359px; background: linear-gradient(135deg, #a8603a, #c98a4a 50%, #9a5330); }
  .photo-library { left: 761px; width: 359px; background: linear-gradient(135deg, #7d4b2e, #a9866a 50%, #5d7fa8); }
  .cta {
    position: absolute; z-index: 2;
    left: 358px; top: 619px; width: 424px; height: 48px;
    background: var(--white); border-radius: 18px;
    text-align: center; color: var(--navy);
    font-size: 17px; font-weight: 500; line-height: 19.5px; padding-top: 5px;
    white-space: nowrap;
  }
  .cta strong { font-weight: 700; }
  .contact-bar {
    position: absolute; z-index: 1;
    left: 241px; top: 661px; width: 652px; height: 58px;
    background: var(--navy); color: var(--white);
    display: flex; align-items: center; justify-content: center; gap: 8px;
    padding-top: 6px;
    font-weight: 900; font-size: 28px; letter-spacing: -0.6px;
    white-space: nowrap;
  }
  .contact-bar svg { width: 24px; height: 24px; flex: none; }
  .contact-sep { font-weight: 700; margin: 0 4px; }
</style>
</head>
<body>
  <main class="backboard">
    <div class="brand">
      <div class="brand-name"><span class="brand-dot"></span>Duravoss</div>
      <div class="brand-tagline">TRUSTED BY QUEENSLAND SCHOOLS SINCE 1995</div>
    </div>

    <h1 class="headline">Creating Cleaner,<br>Safer Learning Environments</h1>
    <p class="subheadline">Specialists in Education<br>Facility Cleaning &amp; Eco-Friendly Services</p>

    <div class="band"></div>
    <div class="band-rule"></div>

    <section class="feature" style="left:274px">
      <div class="feature-badge">
        <svg viewBox="0 0 86 86" fill="none" stroke="#1e3f66" stroke-width="3.5" stroke-linejoin="round" stroke-linecap="round">
          <circle cx="43" cy="36" r="27"/>
          <circle cx="43" cy="36" r="17"/>
          <path d="M43 27l3 6.5 7 .6-5.3 4.6 1.6 6.8L43 42l-6.3 3.5 1.6-6.8L33 34.1l7-.6z"/>
          <path d="M25 56 17 76l10-3 5 9 7-19"/>
          <path d="M61 56l8 20-10-3-5 9-7-19"/>
        </svg>
      </div>
      <p class="feature-text">Over <strong>30 years of expertise</strong> in<br>commercial cleaning</p>
    </section>

    <section class="feature" style="left:603px">
      <div class="feature-badge">
        <svg viewBox="0 0 86 86" fill="none" stroke="#1e3f66" stroke-width="3.5" stroke-linejoin="round" stroke-linecap="round">
          <path d="M43 4 58 10v12c0 10-7 16-15 19-8-3-15-9-15-19V10z"/>
          <path d="M36 22l5 5 9-10"/>
          <path d="M8 50l10-10 12 14-10 9z"/>
          <path d="M78 50 68 40 56 54l10 9z"/>
          <path d="M30 54l10-7h8l8 7"/>
          <path d="M24 60l16 16c3 3 7 0 5-3M32 64l12 11M38 60l11 10c3 2 6-1 4-4"/>
        </svg>
      </div>
      <p class="feature-text">Trusted by <strong>schools, universities,</strong><br><strong>and TAFEs</strong> across Queensland</p>
    </section>

    <section class="feature" style="left:917px">
      <div class="feature-badge">
        <svg viewBox="0 0 86 86" fill="none" stroke="#1e3f66" stroke-width="3.5" stroke-linejoin="round" stroke-linecap="round">
          <circle cx="14" cy="18" r="9"/>
          <path d="M10 18l3 3 5-6"/>
          <circle cx="14" cy="44" r="9"/>
          <path d="M10 44l3 3 5-6"/>
          <path d="M32 13h30M32 23h30M32 40h16"/>
          <path d="M40 80c6-14 18-24 30-28" />
          <path d="M42 76c-4-14 6-26 36-30-2 22-14 34-36 30z" fill="#1e3f66"/>
        </svg>
      </div>
      <p class="feature-text">100% <strong>Carbon Neutral and</strong><br><strong>Eco-Certified</strong> Services</p>
    </section>

    <div class="photo photo-classroom" role="img" aria-label="Photo: bright classroom with teacher and students working at laptops"></div>
    <div class="photo photo-welcome" role="img" aria-label="Photo: teacher welcoming students at a classroom door"></div>
    <div class="photo photo-library" role="img" aria-label="Photo: students collaborating among library bookshelves"></div>

    <p class="cta">Visit us to discuss your school’s cleaning needs<br>and book a <strong>FREE</strong> consultation</p>

    <div class="contact-bar">
      <svg viewBox="0 0 24 24" fill="#2f8ad8"><path d="M6.6 10.8a15.1 15.1 0 0 0 6.6 6.6l2.2-2.2c.3-.3.7-.4 1-.2 1.1.4 2.3.6 3.6.6.6 0 1 .4 1 1V20c0 .6-.4 1-1 1A17 17 0 0 1 3 4c0-.6.4-1 1-1h3.5c.6 0 1 .4 1 1 0 1.3.2 2.5.6 3.6.1.3 0 .7-.2 1z"/></svg>
      <span>1300 649 315</span>
      <span class="contact-sep">|</span>
      <svg viewBox="0 0 24 24" fill="none" stroke="#2f8ad8" stroke-width="1.6"><circle cx="12" cy="12" r="10"/><ellipse cx="12" cy="12" rx="4.5" ry="10"/><path d="M2 12h20M4 6.5h16M4 17.5h16"/></svg>
      <span>www.duravoss.com.au</span>
    </div>
  </main>
</body>
</html>
```